Travel Company is looking for a STAND OUT Business Card

I need a unique Business Card that will truly stand out. Nothing too busy. Simple is good, right? Not looking for a standard design either. No cookie cutter layout. We are a Travel Company that works more with Companies than Travelers. I had an idea to focus and emphasis on the 2 logo a bit more. This is not necessary, however thought it would look interesting. I am just looking for something interesting and a bit different. Does't have to completely off the wall crazy, just not your run of the mill business card.

Target Market(s)

Hoteliers, Resort Management, Call Centers, Executives, Travelers, Families, Businesses

Industry/Entity Type

Hospitality

Contact Information for Business Card

President/CEO - Marcus T Bellamy (title not necessary if design doesn't allow for it)
contact - (407) 555-0186
email - mbellamy@wayfarenow.example
address - 4812 Quillmore Ave #164
Orlando, FL 32804
website - www.wayfarenow.example

Font styles to use
Serif
Other font styles liked:
• Avenir Next LT Pro BOLD

Requirements
Must have
• simple look and design. Unique design
Nice to have
• I attached the 2 logo separate from the main logo. This can be used separately from the Main Logo, together with the main logo or as main logo. I included the logo font. Use it or not, designers choice.
Should not have
• cookie cutter design. Little use of red other than the logo

```html
<!DOCTYPE html>
<html lang="en">
<head>
<meta charset="utf-8">
<title>Wayfarenow Business Card</title>
<link rel="stylesheet" href="https://fonts.googleapis.com/css2?family=Open+Sans:wght@400;600;800&display=swap">
<style>
  :root {
    --backdrop: #8b6b47;
    --card-white: #f4f4f4;
    --card-black-top: #4a4a4a;
    --card-black-bottom: #141414;
    --ink: #111111;
    --ink-soft: #2b2b2b;
    --text-light: #f1f1f1;
    --brand-red: #e00000;
  }
  html, body {
    margin: 0;
    padding: 0;
    width: 1200px;
    height: 1023px;
    overflow: hidden;
    background: var(--backdrop);
    font-family: "Open Sans", Arial, sans-serif;
  }
  .canvas {
    position: relative;
    width: 1200px;
    height: 1023px;
  }
  .card {
    position: absolute;
    width: 720px;
    height: 412px;
    border-radius: 22px;
    box-sizing: border-box;
    overflow: hidden;
  }
  .card--front {
    left: 60px;
    top: 60px;
    background: linear-gradient(135deg, #ffffff 0%, var(--card-white) 60%, #e4e4e4 100%);
  }
  .card--back {
    left: 420px;
    top: 551px;
    background: radial-gradient(ellipse at 30% 20%, var(--card-black-top) 0%, #262626 55%, var(--card-black-bottom) 100%);
    color: var(--text-light);
  }
  .wordmark {
    position: absolute;
    display: flex;
    align-items: center;
    gap: 12px;
    font-weight: 800;
    letter-spacing: -1.5px;
    line-height: 1;
  }
  .wordmark__dot {
    width: 22px;
    height: 22px;
    border-radius: 50%;
    background: var(--brand-red);
    flex: none;
  }
  .card--front .wordmark {
    left: 60px;
    top: 250px;
    font-size: 54px;
    color: var(--ink);
  }
  .front__url {
    position: absolute;
    left: 94px;
    top: 334px;
    font-size: 17px;
    letter-spacing: 4px;
    color: var(--ink-soft);
  }
  .card--back .wordmark {
    left: 60px;
    top: 70px;
    font-size: 64px;
    color: var(--text-light);
  }
  .holder {
    position: absolute;
    right: 48px;
    top: 178px;
    text-align: right;
  }
  .holder__name {
    font-size: 30px;
    font-weight: 600;
    margin: 0;
    line-height: 1.1;
  }
  .holder__title {
    font-size: 17px;
    color: var(--brand-red);
    margin: 2px 0 0;
  }
  .contact {
    position: absolute;
    right: 48px;
    bottom: 40px;
    list-style: none;
    margin: 0;
    padding: 0;
    text-align: right;
    font-size: 16px;
    letter-spacing: 1.2px;
    line-height: 1.45;
  }
  .contact__item {
    display: flex;
    justify-content: flex-end;
    align-items: flex-start;
    gap: 12px;
  }
  .contact__icon {
    width: 16px;
    height: 16px;
    margin-top: 4px;
    flex: none;
  }
  .contact__icon--blank { visibility: hidden; }
</style>
</head>
<body>
<main class="canvas">

  <section class="card card--front" aria-label="Card front">
    <div class="wordmark"><span class="wordmark__dot"></span><span>wayfarenow</span></div>
    <div class="front__url">www.wayfarenow.example</div>
  </section>

  <section class="card card--back" aria-label="Card back">
    <div class="wordmark"><span class="wordmark__dot"></span><span>wayfarenow</span></div>

    <div class="holder">
      <h1 class="holder__name">Marcus T Bellamy</h1>
      <p class="holder__title">President/CEO</p>
    </div>

    <ul class="contact">
      <li class="contact__item">
        <span>(407) 555-0186</span>
        <svg class="contact__icon" viewBox="0 0 16 16" aria-hidden="true">
          <circle cx="8" cy="8" r="7" fill="none" stroke="#e00000" stroke-width="1.4"/>
          <path d="M5.4 4.6c.4-.3.9-.2 1.1.2l.6 1.2c.2.4 0 .7-.3 1l-.4.3c.4.9 1.1 1.6 2 2l.3-.4c.3-.3.6-.5 1-.3l1.2.6c.4.2.5.7.2 1.1-.6.8-1.5 1-2.4.6-1.7-.7-3-2-3.7-3.7-.4-.9-.2-1.8.4-2.6z" fill="#e00000"/>
        </svg>
      </li>
      <li class="contact__item">
        <span>mbellamy@wayfarenow.example</span>
        <svg class="contact__icon" viewBox="0 0 16 16" aria-hidden="true">
          <rect x="1.5" y="3.5" width="13" height="9" fill="none" stroke="#e00000" stroke-width="1.4"/>
          <path d="M1.5 3.5 8 9l6.5-5.5" fill="none" stroke="#e00000" stroke-width="1.4"/>
        </svg>
      </li>
      <li class="contact__item">
        <span>4812 Quillmore Ave #164</span>
        <svg class="contact__icon" viewBox="0 0 16 16" aria-hidden="true">
          <path d="M8 1a5 5 0 0 0-5 5c0 3.8 5 9 5 9s5-5.2 5-9a5 5 0 0 0-5-5z" fill="#e00000"/>
          <circle cx="8" cy="6" r="1.8" fill="#1c1c1c"/>
        </svg>
      </li>
      <li class="contact__item">
        <span>Orlando, FL 32804</span>
        <svg class="contact__icon contact__icon--blank" viewBox="0 0 16 16" aria-hidden="true"></svg>
      </li>
    </ul>
  </section>

</main>
</body>
</html>
```